Business Card Design

Ridge To Ridge The Amber Hearth is a specialist spit roast catering service, equipped with mobile facilities and professional staff to host your function, inside or out.

We cater for all occasions including weddings, birthdays, corporate functions, sporting events and more.

The Amber Hearth was established in 1983 and is now one of Australia's largest and fastest growing spit roast caterers, with franchises Australia wide, attributing its outstanding success to quality, professionalism and exceptional customer service.

Ridge to Ridge The Amber Hearth is your complete catering solution. We prepare, cook and present the food, allowing you to completely enjoy your function and entertain your guests. We even clean up after ourselves and package any unconsumed foods for your continued enjoyment.

Choose your Amber Hearth menu from premium cuts of pork, lamb, beef, chicken and baked ham, spit roasted to perfection creating mouth watering flavours. All meats are provided by leading local butchers and are cooked on-site to ensure quality and freshness.

Our professionally trained staff also provide complimentary tea and coffee with your function and are pleased to accommodate special dietary requests. Ridge To Ridge The Amber Hearth also provides plates, cups, cutlery and serviettes in the colour of your choice.

Renowned for our generous servings, we never run out of food, for numbers quoted, and what is not consumed, remains with you. We are dedicated to ensuring your function is catered for professionally, with unbeatable value. There is absolutely no compromise on quality, quantity or presentation.

Further options include hot or cold pre-dinner nibbles and Ridge to Ridge The Amber Hearth are equipped to cater for up to 5,000 guests.

Industry/Entity Type

Catering

Contact Information for Business Card

Marek Pellow
PH: 1300 482 917
M: 0412 358 204
Email: northbay@amberhearth.com.au
www.amberhearth.com.au/northbay

Trusted Spit Roast & Function Caterers Across Australia

```html
<!DOCTYPE html>
<html lang="en">
<head>
<meta charset="utf-8">
<title>The Amber Hearth – Business Card</title>
<link rel="stylesheet" href="https://fonts.googleapis.com/css2?family=Open+Sans:wght@400;600;700&display=swap">
<style>
  :root {
    --backdrop: #e9e6e1;
    --card: #f4f4f4;
    --ink: #4a4a4a;
    --ink-soft: #5c5c5c;
    --accent: #c9574b;
    --band: #d6d334;
    --band-ink: #4f4a16;
  }
  * { box-sizing: border-box; margin: 0; padding: 0; }
  html, body {
    width: 1200px; height: 900px; overflow: hidden;
    background: var(--backdrop);
    font-family: "Open Sans", Arial, sans-serif;
  }
  .card {
    position: absolute; left: 150px; top: 175px;
    width: 900px; height: 550px;
    background: var(--card);
    box-shadow: 0 10px 30px rgba(0,0,0,.18);
    overflow: hidden;
  }
  .brand {
    position: absolute; left: 60px; top: 110px;
    display: flex; align-items: center; gap: 12px;
  }
  .brand-mark {
    flex: none; width: 18px; height: 18px;
    background: var(--ink);
  }
  .brand-name {
    font-weight: 600; font-size: 26px; line-height: 1.2;
    color: var(--ink);
    white-space: nowrap;
  }
  .person {
    position: absolute; left: 440px; top: 170px;
    font-weight: 700; font-size: 34px; color: var(--ink);
    letter-spacing: .5px;
  }
  .contacts {
    position: absolute; left: 385px; top: 245px;
    list-style: none;
  }
  .contacts li {
    display: flex; align-items: center; gap: 18px;
    height: 40px;
    font-size: 21px; color: var(--ink-soft);
  }
  .contacts svg { width: 20px; height: 20px; flex: none; }
  .band {
    position: absolute; left: 0; right: 0; bottom: 0; height: 95px;
    background: var(--band);
    display: flex; align-items: center; padding-left: 45px;
  }
  .tagline {
    font-weight: 700; font-size: 25px; color: var(--band-ink);
    white-space: nowrap;
  }
</style>
</head>
<body>
  <div class="card">
    <div class="brand">
      <span class="brand-mark"></span>
      <span class="brand-name">The Amber Hearth</span>
    </div>

    <div class="person">Marek Pellow</div>

    <ul class="contacts">
      <li>
        <svg viewBox="0 0 20 20" aria-hidden="true"><path d="M4 2h4l1.5 4-2.2 1.4a10 10 0 0 0 5.3 5.3L14 10.5l4 1.5v4a2 2 0 0 1-2 2A14 14 0 0 1 2 4a2 2 0 0 1 2-2z" fill="none" stroke="var(--accent)" stroke-width="1.6"/></svg>
        1300 482 917
      </li>
      <li>
        <svg viewBox="0 0 20 20" aria-hidden="true"><rect x="5.5" y="1.5" width="9" height="17" rx="1.5" fill="none" stroke="var(--accent)" stroke-width="1.6"/><circle cx="10" cy="15.5" r="1" fill="var(--accent)"/></svg>
        0412 358 204
      </li>
      <li>
        <svg viewBox="0 0 20 20" aria-hidden="true"><rect x="1.5" y="4" width="17" height="12" fill="none" stroke="var(--accent)" stroke-width="1.6"/><path d="M1.5 4l8.5 7 8.5-7" fill="none" stroke="var(--accent)" stroke-width="1.6"/></svg>
        northbay@amberhearth.com.au
      </li>
      <li>
        <svg viewBox="0 0 20 20" aria-hidden="true"><circle cx="10" cy="10" r="8" fill="none" stroke="var(--accent)" stroke-width="1.6"/><ellipse cx="10" cy="10" rx="3.5" ry="8" fill="none" stroke="var(--accent)" stroke-width="1.4"/><path d="M2 10h16" stroke="var(--accent)" stroke-width="1.4"/></svg>
        www.amberhearth.com.au/northbay
      </li>
    </ul>

    <div class="band">
      <p class="tagline">Trusted Spit Roast &amp; Function Caterers Across Australia</p>
    </div>
  </div>
</body>
</html>
```